Etiquette pour pots de Miel de Kolvera
Besoins
Nous souhaitons créer une étiquette pour notre Miel de Kolvera, produit et commercialisé en République Démocratique du Congo.
Ce miel s’apparente à une qualité bio car les ruches se trouvent en pleine nature, loin des villes et de la pollution.
Les caractéristiques du flacon sont les suivantes (photo ci-joint) :
Hauteur : 12 cm
Circonférence (mi-hauteur) : 34 cm
Diamètre (ouverture supérieure) : 8 cm
Contenance : 660 ml.
La taille de l’étiquette est laissée à la libre appréciation du graphiste.
L’étiquette doit évoquer le côté sain/circuit court/bio et la qualité.
Les éléments suivants doivent être présents sur l’étiquette :
1. Nom du produit :
MIEL DE KOLVERA
ASALI YA KOLVERA (traduction en swahili)
2. Eléments : abeille stylisée, fleurs
3. Logo Tumsoa (ci-joint)
4. Producteur : Ranch de Kolvera
5. Miel Bio des plateaux de Kolvera
6. 660 ml

```html
<!DOCTYPE html>
<html lang="fr">
<head>
<meta charset="utf-8">
<title>Etiquette – Miel de Kolvera</title>
<link href="https://fonts.googleapis.com/css2?family=Dancing+Script:wght@600&family=Patrick+Hand&family=Montserrat:wght@500;700&display=swap" rel="stylesheet">
<style>
  :root{
    --green:#7dbb2e;
    --green-dark:#5e9c1f;
    --green-tab:#8cc63f;
    --lime:#d9e84c;
    --cream:#fbf4da;
    --honey:#e8962a;
    --honey-soft:#f4cf78;
    --leaf-soft:#d8e6a8;
    --paper:#ffffff;
    --rule:#d6d6d6;
  }
  html,body{margin:0;padding:0;overflow:hidden;background:var(--paper);}
  .canvas{width:1200px;height:742px;position:relative;overflow:hidden;}
  .canvas svg{display:block;}
  .script{font-family:"Dancing Script",cursive;font-weight:600;}
  .hand{font-family:"Patrick Hand",cursive;}
  .sans{font-family:"Montserrat",Arial,sans-serif;}
  .title{fill:var(--paper);font-size:46px;}
  .swahili{fill:var(--honey);font-size:24px;}
  .volume{fill:var(--green-dark);font-size:17px;font-weight:700;}
  .origin{fill:var(--paper);font-size:19px;font-weight:700;}
  .producer{fill:#eef7d8;font-size:12px;font-weight:500;}
  .partner{fill:var(--green-dark);font-size:12px;font-weight:700;letter-spacing:.5px;}
  .lid-title{fill:var(--paper);font-size:25px;}
  .lid-origin{fill:var(--paper);font-size:9.5px;font-weight:500;}
  .lid-volume{fill:var(--paper);font-size:14px;font-weight:700;}
</style>
</head>
<body>
<div class="canvas">
<svg width="1200" height="742" viewBox="0 0 1200 742" xmlns="http://www.w3.org/2000/svg">
  <defs>
    <linearGradient id="band-fill" x1="0" x2="1" y1="0" y2="0">
      <stop offset="0" stop-color="var(--green)"/>
      <stop offset="0.5" stop-color="var(--lime)"/>
      <stop offset="1" stop-color="var(--green)"/>
    </linearGradient>
    <radialGradient id="lid-fill" cx="0.5" cy="0.5" r="0.5">
      <stop offset="0" stop-color="var(--lime)"/>
      <stop offset="1" stop-color="var(--green)"/>
    </radialGradient>
    <linearGradient id="artwork-fill" x1="0" x2="0" y1="0" y2="1">
      <stop offset="0" stop-color="var(--honey-soft)"/>
      <stop offset="0.55" stop-color="var(--cream)"/>
      <stop offset="1" stop-color="var(--leaf-soft)"/>
    </linearGradient>
  </defs>

  <g class="wrap-label">
    <rect class="label-edge" x="10" y="80" width="1180" height="350" fill="var(--paper)" stroke="var(--rule)" stroke-width="1.5"/>
    <path class="top-tab" d="M290 122 C332 122 330 42 382 42 L818 42 C870 42 868 122 910 122 Z" fill="var(--green)"/>
    <rect class="band" x="10" y="112" width="1180" height="238" fill="url(#band-fill)"/>
    <path class="bottom-tab" d="M300 348 C342 348 340 428 392 428 L808 428 C860 428 858 348 900 348 Z" fill="var(--green-tab)"/>

    <text class="script title" x="600" y="94" text-anchor="middle">Miel de Kolvera</text>

    <g class="medallion">
      <circle cx="612" cy="238" r="104" fill="var(--cream)"/>
      <circle cx="612" cy="238" r="104" fill="none" stroke="var(--cream)" stroke-width="14" stroke-linecap="round" stroke-dasharray="0 21.8"/>
      <g role="img" aria-label="Abeille stylisée butinant des fleurs">
        <rect x="548" y="156" width="128" height="160" rx="40" fill="url(#artwork-fill)" opacity="0.75"/>
      </g>
      <text class="hand swahili" x="652" y="256" text-anchor="middle">Asali</text>
      <text class="hand swahili" x="642" y="277" text-anchor="middle">Ya Kolvera</text>
    </g>

    <g class="organic-badge">
      <circle cx="508" cy="222" r="42" fill="var(--green)" stroke="var(--paper)" stroke-width="5"/>
    </g>

    <g class="partner-mark">
      <circle cx="746" cy="322" r="38" fill="var(--paper)"/>
      <text class="sans partner" x="746" y="326" text-anchor="middle">Tumsoa</text>
    </g>

    <rect class="volume-box" x="560" y="352" width="80" height="25" rx="5" fill="var(--paper)"/>
    <text class="sans volume" x="600" y="370" text-anchor="middle">660 ml</text>
    <text class="sans origin" x="600" y="397" text-anchor="middle">Miel Bio des plateaux de Kolvera</text>
    <text class="sans producer" x="600" y="416" text-anchor="middle">Producteur : Ranch de Kolvera</text>
  </g>

  <g class="lid-label">
    <circle cx="600" cy="596" r="128" fill="var(--paper)" stroke="var(--rule)" stroke-width="1.5"/>
    <circle cx="600" cy="596" r="106" fill="url(#lid-fill)"/>
    <circle cx="600" cy="596" r="106" fill="none" stroke="var(--green)" stroke-width="12" stroke-linecap="round" stroke-dasharray="0 20.8"/>
    <text class="script lid-title" x="600" y="545" text-anchor="middle">Miel de Kolvera</text>
    <text class="sans lid-origin" x="600" y="562" text-anchor="middle">Miel Bio des plateaux de Kolvera</text>
    <circle class="organic-badge" cx="600" cy="598" r="27" fill="var(--green)" stroke="var(--paper)" stroke-width="4"/>
    <line x1="548" y1="636" x2="652" y2="636" stroke="var(--paper)" stroke-width="1.2"/>
    <text class="sans lid-volume" x="600" y="658" text-anchor="middle">660 ml</text>
  </g>
</svg>
</div>
</body>
</html>
```